Global Corvane Power Technology Company needs initial Web Design

We need a web design for new Corvane Power Technology company. The company has developed innovative technology and needs a website to reflect this branding. Whilst this assignment will represent the initial site we are seeking an ongoing relationship to allow the website to be developed as the business develops. The logo design and initial artwork has been done and needs to incorporated in the design.

Target Market(s)

Business decision makers and power generation companies
Initially two target markets
1. Commercial users like construction companies or industrial businesses like mining that currently utilize Diesel generators to create power
2. Electrical power suppliers that currently use diesel generators in regional and remote to supply remote communities like outback Australia or pacific islands like Fuji etc
The purpose initially is to showcase/ educate customers about the product but we ideally would like to capture email addressees as part of this process.

The product information has been limited at this stage as we are currently finalizing IP registrations.

The main competitors are
1 Solar energy products but these only generate power when the sun is shinning and needs to be stored which battery technology is expensive and will only last up to 3 days at most
2 Wind energy would the same as as solar
3 Diesel generators run continually but are expensive to operate. Our product would be approximately 1/2 the operating cost of this energy source. There is no reliance on fuel sources so the user doesn't need to store fuel, worry about running out or fluctuations in fuel pricing. Diesel generators are very noisy and not environmentally friendly.

Industry/Entity Type

Solar Energy

Coding

Coded - Design and coding required

Number of Pages Required

4 page

Font styles to use
Sans Serif

Colors
acd036
33a6d7
ffffff

Requirements
Must have
• This version is intended as an initial basic 4 page website only.
• It should be built on the basis that it can be expanded after the products are formally launched into the market. A separate assignment will be allocated to the successful initial website designer to create a more elaborate site with a budget to match. The format and content for the initial site is outlined in the attached word document (File 1) The remaining files contain the logo and existing artwork and associated colours. The site should have the ability to view on smart phones and tablets.

```html
<!DOCTYPE html>
<html lang="en">
<head>
<meta charset="utf-8">
<title>Corvane Power</title>
<link rel="stylesheet" href="https://fonts.googleapis.com/css2?family=Raleway:wght@500;600;700&family=Open+Sans:wght@400;600&display=swap">
<style>
:root{
  --green:#acd036;
  --green-dark:#8fbf1f;
  --blue:#33a6d7;
  --navy:#1a6a96;
  --ink:#222;
  --nav:#444;
  --muted:#555;
  --white:#ffffff;
  --sky-top:#6fb3ea;
  --sky-bottom:#eef5fb;
}
*{margin:0;padding:0;box-sizing:border-box}
html,body{width:1110px;height:1200px;overflow:hidden;background:var(--white)}
body{position:relative;font-family:'Open Sans',sans-serif;color:var(--ink)}
.site-header{position:absolute;left:0;top:0;width:1110px;height:75px;background:var(--white);border-bottom:1px solid #e3e3e3}
.brand{position:absolute;left:201px;top:17px;display:flex;align-items:center;gap:10px}
.brand-mark{width:44px;height:44px;border-radius:50%;background:var(--blue)}
.brand-name{font-family:'Raleway',sans-serif;font-weight:700;font-size:20px;color:var(--green);letter-spacing:.5px}
.main-nav{position:absolute;top:32px;left:0;font-family:'Raleway',sans-serif;font-weight:500;font-size:11.5px}
.main-nav a{position:absolute;white-space:nowrap;color:var(--nav);text-decoration:none}
.main-nav a.active{color:var(--green)}
.hero{position:absolute;left:0;top:75px;width:1110px;height:410px;background:linear-gradient(180deg,var(--sky-top) 0%,#a9d2f3 35%,#dcebf7 70%,var(--sky-bottom) 100%);border-bottom:1px solid #dcdcdc}
.hero-title{position:absolute;left:199px;top:115px;font-family:'Raleway',sans-serif;font-weight:600;font-size:29px;color:var(--navy)}
.hero-sub{position:absolute;left:199px;top:157px;font-family:'Raleway',sans-serif;font-weight:500;font-size:16px;color:var(--navy)}
.hero-text{position:absolute;left:199px;top:187px;width:360px;font-size:8.5px;line-height:14px;color:#444}
.btn-read{position:absolute;left:199px;top:231px;width:101px;height:31px;background:var(--green);color:var(--white);font-family:'Raleway',sans-serif;font-weight:700;font-size:11px;line-height:31px;text-align:center}
.slider-dots{position:absolute;left:200px;top:278px;display:flex;gap:4px}
.slider-dots span{width:13px;height:13px;border-radius:50%;background:#9a9a9a}
.slider-dots span.on{background:var(--blue)}
.hero-product{position:absolute;left:630px;top:47px;width:300px;height:325px;background:linear-gradient(135deg,#f1f1f1 0%,#d9d9d9 40%,#3aa7d8 75%,#1d1d1d 100%);border-radius:4px}
.features{position:absolute;left:118px;top:486px;width:874px;height:344px;background:linear-gradient(180deg,#fff 75%,#efefef 100%)}
.feature{position:absolute;width:180px;text-align:center}
.feature svg{display:block;margin:0 auto;width:36px;height:36px}
.feature h3{margin-top:10px;font-family:'Raleway',sans-serif;font-weight:500;font-size:13.5px;color:var(--ink);white-space:nowrap}
.feature p{margin-top:6px;font-size:8.5px;line-height:15px;color:var(--muted)}
.about{position:absolute;left:195px;top:868px;width:431px}
.about h2{font-family:'Raleway',sans-serif;font-weight:500;font-size:23px;color:#333;margin-bottom:14px}
.about p{font-size:8.8px;line-height:15.5px;color:#555;margin-bottom:9px}
.about-visual{position:absolute;left:645px;top:876px;width:255px;height:180px;background:linear-gradient(135deg,#e9f1f6 0%,#bcd7e6 45%,#a5cf3a 75%,#e23b2b 100%);border-radius:4px}
.site-footer{position:absolute;left:0;top:1105px;width:1110px;height:95px;background:linear-gradient(180deg,var(--green) 0%,#8dc22a 100%)}
.foot-nav a{position:absolute;top:26px;font-family:'Raleway',sans-serif;font-weight:600;font-size:10.5px;color:var(--white);text-decoration:none;white-space:nowrap}
.copyright{position:absolute;left:201px;top:48px;font-size:8.5px;color:var(--white)}
.social{position:absolute;left:835px;top:26px;display:flex;gap:9px}
.social span{width:13px;height:13px;border-radius:50%;background:var(--white)}
</style>
</head>
<body>
<header class="site-header">
  <div class="brand"><span class="brand-mark"></span><span class="brand-name">CORVANE POWER</span></div>
  <nav class="main-nav">
    <a class="active" href="#" style="left:539px">HOME</a>
    <a href="#" style="left:607px">OUR PRODUCTS</a>
    <a href="#" style="left:731px">OUR PEOPLE</a>
    <a href="#" style="left:837px">CONTACT US</a>
  </nav>
</header>

<section class="hero">
  <h1 class="hero-title">Corvane Power</h1>
  <p class="hero-sub">Sed metus augue convallis vehicula</p>
  <p class="hero-text">In massa libero interdum nec interdum vel blandit sed nulla In ullamcorper est eget tempor cursus neque mi consectetuer mi a ultricies massa est sed</p>
  <a class="btn-read">READ MORE</a>
  <div class="slider-dots"><span class="on"></span><span></span><span></span><span></span></div>
  <div class="hero-product" role="img" aria-label="Photo of the white and blue portable power generator unit"></div>
</section>

<section class="features">
  <div class="feature" style="left:67px;top:36px">
    <svg viewBox="0 0 36 36"><path d="M11 9a12 12 0 1 0 14 0" fill="none" stroke="#acd036" stroke-width="4" stroke-linecap="round"/><line x1="18" y1="3" x2="18" y2="17" stroke="#acd036" stroke-width="4" stroke-linecap="round"/></svg>
    <h3>24 hour a day power</h3>
    <p>Pellentesque faucibus Ut accumsan<br>ultricies elit Maecenas justo</p>
  </div>
  <div class="feature" style="left:250px;top:36px">
    <svg viewBox="0 0 36 36"><path d="M18 4C14 12 10 17 10 23a8 8 0 0 0 16 0c0-6-4-11-8-19z" fill="#acd036"/></svg>
    <h3>No fuel sources</h3>
    <p>Pellentesque faucibus Ut accumsan<br>ultricies elit Maecenas justo</p>
  </div>
  <div class="feature" style="left:436px;top:34px">
    <svg viewBox="0 0 36 36"><path d="M18 34V12" stroke="#acd036" stroke-width="3"/><ellipse cx="18" cy="7" rx="4" ry="6" fill="#acd036"/><ellipse cx="10" cy="17" rx="7" ry="3.5" transform="rotate(30 10 17)" fill="#acd036"/><ellipse cx="26" cy="17" rx="7" ry="3.5" transform="rotate(-30 26 17)" fill="#acd036"/><ellipse cx="10" cy="27" rx="6" ry="3" transform="rotate(-20 10 27)" fill="#acd036"/></svg>
    <h3>Environmentally friendly</h3>
    <p>Pellentesque faucibus Ut accumsan<br>ultricies elit Maecenas justo</p>
  </div>
  <div class="feature" style="left:628px;top:36px">
    <svg viewBox="0 0 36 36"><path d="M28 12A12 12 0 1 0 30 20" fill="none" stroke="#acd036" stroke-width="5"/><path d="M22 4l10 2-2 10z" fill="#acd036"/></svg>
    <h3>Scalable and relocatable</h3>
    <p>Pellentesque faucibus Ut accumsan<br>ultricies elit Maecenas justo</p>
  </div>
  <div class="feature" style="left:67px;top:172px">
    <svg viewBox="0 0 36 36"><rect x="12" y="8" width="14" height="16" rx="3" transform="rotate(35 19 16)" fill="#acd036"/><path d="M15 24L5 34" stroke="#acd036" stroke-width="4" stroke-linecap="round"/><path d="M22 6l5-5M29 13l5-5" stroke="#acd036" stroke-width="3" stroke-linecap="round"/></svg>
    <h3>Quick and easy installation</h3>
    <p>Pellentesque faucibus Ut accumsan<br>ultricies elit Maecenas justo</p>
  </div>
  <div class="feature" style="left:250px;top:172px">
    <svg viewBox="0 0 36 36"><path d="M8 30L22 16" stroke="#acd036" stroke-width="6" stroke-linecap="round"/><circle cx="25" cy="11" r="8" fill="#acd036"/><circle cx="28" cy="8" r="4" fill="#fff"/></svg>
    <h3>Full maintenance support</h3>
    <p>Pellentesque faucibus Ut accumsan<br>ultricies elit Maecenas justo</p>
  </div>
  <div class="feature" style="left:436px;top:172px">
    <svg viewBox="0 0 36 36"><circle cx="18" cy="18" r="14" fill="none" stroke="#acd036" stroke-width="4"/><path d="M18 10v9h-6" fill="none" stroke="#acd036" stroke-width="3"/></svg>
    <h3>24 hour monitoring</h3>
    <p>Pellentesque faucibus Ut accumsan<br>ultricies elit Maecenas justo</p>
  </div>
  <div class="feature" style="left:628px;top:166px">
    <svg viewBox="0 0 36 36" style="width:52px;height:42px"><path d="M10 24L4 34l7-2 3 4 5-10zM26 24l6 10-7-2-3 4-5-10z" fill="#acd036"/><circle cx="18" cy="16" r="14" fill="#acd036"/><circle cx="18" cy="16" r="9" fill="#fff"/><circle cx="18" cy="16" r="7.5" fill="#acd036"/><text x="18" y="19.5" text-anchor="middle" font-family="Raleway,sans-serif" font-weight="700" font-size="9" fill="#fff">20</text></svg>
    <h3>20 year&nbsp; warranty</h3>
    <p>Pellentesque faucibus Ut accumsan<br>ultricies elit Maecenas justo</p>
  </div>
</section>

<section class="about">
  <h2>About Our Products</h2>
  <p>Corvane Power has developed patented electric power generation technology that revolutionises the way the world will think about power generation for generations to come.</p>
  <p>The advanced generator technology has been designed in a way that there are minimal&nbsp; energy losses. The generator, coupled with the intelligent mechanical and electronic multipliers, allows the system to produce very high input to output ratios resulting in ratios of 1 to 100 outputs.</p>
  <p>These transportable Units require no external fuel sources making them completely environmentally friendly.&nbsp; Low noise and no emissions enables these environmentally friendly units</p>
</section>
<div class="about-visual" role="img" aria-label="Illustration of an office building with solar roof beside an energy efficiency rating scale"></div>

<footer class="site-footer">
  <nav class="foot-nav">
    <a href="#" style="left:201px">HOME</a>
    <a href="#" style="left:255px">ABOUT US</a>
    <a href="#" style="left:332px">SERVICES</a>
    <a href="#" style="left:405px">FAQ</a>
    <a href="#" style="left:449px">SUPPORT</a>
    <a href="#" style="left:521px">CONTACT</a>
  </nav>
  <p class="copyright">© 2015 Company Name&nbsp; All right reserved&nbsp; Term of Use</p>
  <div class="social"><span></span><span></span><span></span><span></span></div>
</footer>
</body>
</html>
```